Peach Point of Sale Cards for Grocery Retail Markets

We are looking to update our peach point of sale card and price card. The cards will need to be 7" x 11" with a .125 bleed - one sided. See attached for the old versions. We would like this to use photos that look like true Washington State Peaches. Here are the bullet points we would like to use: - New Crop!- Tree Ripened- Excellent FlavorNOTE: The price card just needs to have a space where a retailer can write in the sale price of the item. See attachment with the white box.

Target Market(s)

Retail market shoppers

Requirements
Must have
• Pictures of Peaches Only

```html
<!DOCTYPE html>
<html lang="en">
<head>
<meta charset="utf-8">
<title>Washington State Peaches – Point of Sale Card</title>
<link href="https://fonts.googleapis.com/css2?family=Oswald:wght@600;700&family=Kanit:ital,wght@1,700;1,800;1,900&display=swap" rel="stylesheet">
<style>
  :root {
    --olive: #a3ae25;
    --panel-light: #ffffff;
    --panel-shade: #e3e3e3;
    --cocoa: #9c6b5a;
    --blush: #e9a797;
    --leaf-green: #9cb22a;
    --leaf-light: #b7c936;
    --coral: #f2543f;
    --white: #ffffff;
    --peach-deep: #c4473c;
    --peach-mid: #e8866a;
    --peach-rose: #d9645a;
    --peach-light: #f3c79a;
    --peach-cream: #f7dcb4;
  }
  html, body {
    margin: 0;
    padding: 0;
    width: 1200px;
    height: 764px;
    overflow: hidden;
    background: var(--white);
  }
  .pos-card {
    position: relative;
    width: 1200px;
    height: 764px;
    overflow: hidden;
  }
  .produce-photo {
    position: absolute;
    inset: 0;
    background:
      radial-gradient(circle at 64% 30%, var(--peach-cream) 0 5%, var(--peach-mid) 14%, transparent 20%),
      radial-gradient(circle at 92% 40%, var(--peach-light) 0 6%, var(--peach-mid) 13%, transparent 19%),
      radial-gradient(circle at 52% 12%, var(--peach-light) 0 4%, var(--peach-rose) 11%, transparent 16%),
      radial-gradient(circle at 82% 10%, var(--peach-mid) 0 6%, var(--peach-rose) 12%, transparent 17%),
      radial-gradient(circle at 48% 60%, var(--peach-mid) 0 6%, var(--peach-deep) 13%, transparent 18%),
      radial-gradient(circle at 74% 58%, var(--peach-rose) 0 5%, var(--peach-deep) 11%, transparent 16%),
      radial-gradient(circle at 70% 88%, var(--peach-cream) 0 5%, var(--peach-mid) 14%, transparent 20%),
      radial-gradient(circle at 95% 85%, var(--peach-light) 0 4%, var(--peach-mid) 12%, transparent 17%),
      radial-gradient(circle at 42% 92%, var(--peach-light) 0 4%, var(--peach-mid) 12%, transparent 17%),
      linear-gradient(135deg, var(--peach-mid), var(--peach-rose) 45%, var(--peach-deep) 70%, var(--peach-mid));
  }
  .text-panel {
    position: absolute;
    inset: 0;
    width: 1200px;
    height: 764px;
  }
  .edge-band {
    position: absolute;
    left: 0;
    top: 0;
    width: 30px;
    height: 764px;
    background: var(--olive);
  }
  .headline-new {
    position: absolute;
    left: 76px;
    top: 47px;
    margin: 0;
    font-family: "Oswald", sans-serif;
    font-weight: 700;
    font-size: 113px;
    line-height: 1;
    letter-spacing: -2px;
    color: var(--cocoa);
    text-transform: uppercase;
    white-space: nowrap;
  }
  .headline-new .crop {
    font-weight: 600;
    font-size: 78px;
    letter-spacing: -2px;
    color: var(--blush);
    margin-left: 6px;
  }
  .benefit {
    position: absolute;
    margin: 0;
    font-family: "Kanit", sans-serif;
    font-style: italic;
    line-height: 1;
    white-space: nowrap;
    transform-origin: left top;
  }
  .benefit-tree {
    left: 103px;
    top: 207px;
    font-weight: 800;
    font-size: 100px;
    letter-spacing: -2px;
    color: var(--leaf-green);
    transform: scaleX(0.86);
  }
  .benefit-ripened {
    left: 76px;
    top: 300px;
    font-weight: 800;
    font-size: 82px;
    letter-spacing: -2px;
    color: var(--leaf-green);
    transform: scaleX(0.88);
  }
  .leaf-icon {
    position: absolute;
    left: 286px;
    top: 188px;
    width: 118px;
    height: 132px;
  }
  .benefit-excellent {
    left: 124px;
    top: 410px;
    font-weight: 800;
    font-size: 104px;
    letter-spacing: -2px;
    color: var(--coral);
    -webkit-text-stroke: 3px var(--white);
    paint-order: stroke fill;
    text-shadow: 3px 4px 6px rgba(0,0,0,0.25);
    transform: scaleX(0.84);
  }
  .benefit-flavor {
    left: 76px;
    top: 488px;
    font-weight: 900;
    font-size: 212px;
    letter-spacing: -4px;
    color: var(--coral);
    -webkit-text-stroke: 4px var(--white);
    paint-order: stroke fill;
    text-shadow: 4px 5px 8px rgba(0,0,0,0.25);
    transform: scaleX(0.67);
  }
  .origin {
    position: absolute;
    left: 566px;
    top: 46px;
    width: 500px;
    text-align: center;
    margin: 0;
    font-family: "Oswald", sans-serif;
    font-weight: 700;
    color: var(--white);
    text-transform: uppercase;
    line-height: 1;
  }
  .origin-state {
    display: block;
    font-size: 66px;
    letter-spacing: -1.5px;
    transform: scaleX(0.9);
    text-shadow: 2px 2px 0 var(--coral), -2px -2px 0 var(--coral), 2px -2px 0 var(--coral), -2px 2px 0 var(--coral);
  }
  .origin-fruit {
    display: block;
    margin-top: 6px;
    font-size: 38px;
    font-weight: 700;
    letter-spacing: 1px;
    text-shadow: 1px 1px 3px rgba(0,0,0,0.35);
  }
</style>
</head>
<body>
<main class="pos-card">
  <div class="produce-photo" role="img" aria-label="Close-up photo of a heap of ripe red and yellow Washington peaches with a green leaf"></div>

  <svg class="text-panel" viewBox="0 0 1200 764" aria-hidden="true">
    <defs>
      <linearGradient id="panelFade" x1="0" y1="0" x2="1" y2="0">
        <stop offset="0" stop-color="var(--panel-shade)"/>
        <stop offset="0.55" stop-color="var(--panel-light)"/>
        <stop offset="1" stop-color="var(--panel-light)"/>
      </linearGradient>
    </defs>
    <path d="M0 0 H470 C402 250 398 520 455 764 H0 Z" fill="url(#panelFade)"/>
  </svg>

  <div class="edge-band"></div>

  <h1 class="headline-new">New<span class="crop">Crop.</span></h1>

  <p class="benefit benefit-tree">Tree</p>
  <p class="benefit benefit-ripened">Ripened</p>

  <svg class="leaf-icon" viewBox="0 0 118 132" aria-hidden="true">
    <path d="M6 4 C40 6 58 28 52 58 C28 54 8 36 6 4 Z" fill="var(--leaf-light)"/>
    <path d="M10 10 L48 54" stroke="var(--white)" stroke-width="3" stroke-linecap="round"/>
    <path d="M114 44 C112 92 82 120 36 122 C40 78 70 50 114 44 Z" fill="var(--leaf-green)"/>
    <path d="M106 52 L44 116" stroke="var(--white)" stroke-width="3.5" stroke-linecap="round"/>
  </svg>

  <p class="benefit benefit-excellent">Excellent</p>
  <p class="benefit benefit-flavor">Flavor.</p>

  <h2 class="origin">
    <span class="origin-state">Washington State</span>
    <span class="origin-fruit">Peaches</span>
  </h2>
</main>
</body>
</html>
```